Top label sticker design -Australian Owned

We are seeking to develop a top sticker for our range of batteries, 80mm x 30mm.
Enclosed is the current top label sample, and new label will also be added. The message we want to send is, state that we are "100% Australian Family Owned", would like to use our Ostvane Logo merged with an Australian flag or similar to show the strength and roots of our brand.

Target Market(s)

30 to 50 year old males

Industry/Entity Type

Automotive

Requirements
Must have
• "100% Australian Family Owned" text or similar wording
Ostvane logo
Nice to have
• Blend of Australian flag with/ across our Ostvane logo.
Red background colour, Tellbrook Carriers Red.
Should not have
• To much much fluff, want to achieve a short sharp message.

```html
<!DOCTYPE html>
<html lang="en">
<head>
<meta charset="utf-8">
<title>Ostvane – Top Label Sticker</title>
<link href="https://fonts.googleapis.com/css2?family=Jost:wght@400;600&display=swap" rel="stylesheet">
<style>
  :root {
    --brand-red: #c80000;
    --flag-blue: #00008b;
    --ink-white: #ffffff;
    --mark-tint: rgba(255, 255, 255, 0.22);
    --band-dark: #222222;
    --page-grey: #e3e3e3;
  }
  * { margin: 0; padding: 0; box-sizing: border-box; }
  html, body {
    width: 1200px;
    height: 1051px;
    overflow: hidden;
    background: var(--page-grey);
    font-family: "Jost", "Futura", sans-serif;
  }
  .label {
    position: absolute;
    left: 60px;
    width: 1080px;
    height: 404px;
    background: var(--brand-red);
    box-shadow: 0 10px 40px rgba(0, 0, 0, 0.35);
  }
  .label--light { top: 69px; }
  .label--dark { top: 564px; }

  .brand-name {
    position: absolute;
    left: 0;
    width: 100%;
    top: 70px;
    text-align: center;
    color: var(--ink-white);
    font-weight: 400;
    font-size: 104px;
    line-height: 1;
    letter-spacing: 4px;
  }
  .product-line {
    position: absolute;
    left: 0;
    width: 100%;
    top: 163px;
    text-align: center;
    color: var(--ink-white);
    font-weight: 400;
    font-size: 35px;
    line-height: 1;
    word-spacing: 10px;
  }
  .brand-mark {
    position: absolute;
    left: 352px;
    top: 209px;
    width: 201px;
    height: 112px;
    background: var(--mark-tint);
  }
  .divider {
    position: absolute;
    left: 590px;
    top: 203px;
    width: 1px;
    height: 100px;
    background: rgba(255, 255, 255, 0.7);
  }
  .flag {
    position: absolute;
    left: 632px;
    top: 209px;
    width: 89px;
    height: 62px;
    background: var(--flag-blue);
  }
  .tagline-band {
    position: absolute;
    left: 0;
    bottom: 0;
    width: 100%;
    height: 63px;
    display: flex;
    align-items: center;
    justify-content: center;
    font-weight: 600;
    font-size: 32px;
    letter-spacing: 0.5px;
  }
  .label--light .tagline-band { background: var(--ink-white); color: var(--brand-red); }
  .label--dark .tagline-band { background: var(--band-dark); color: var(--ink-white); }
</style>
</head>
<body>
  <section class="label label--light">
    <div class="brand-name">Ostvane</div>
    <div class="product-line">BATTERIES OILS FILTERS</div>
    <div class="brand-mark" role="img" aria-label="Brand mark area"></div>
    <div class="divider"></div>
    <div class="flag" role="img" aria-label="Australian flag"></div>
    <div class="tagline-band">100% Australian Family Owned</div>
  </section>

  <section class="label label--dark">
    <div class="brand-name">Ostvane</div>
    <div class="product-line">BATTERIES OILS FILTERS</div>
    <div class="brand-mark" role="img" aria-label="Brand mark area"></div>
    <div class="divider"></div>
    <div class="flag" role="img" aria-label="Australian flag"></div>
    <div class="tagline-band">100% Australian Family Owned</div>
  </section>
</body>
</html>
```